Web Developer Needs a Business Card Design

I need a personal business card design that represents me as a web developer for potential employers. I would like the background to be a dark color on the front for contrast with my logo and name. The back will have all my information along with a smaller version of the logo. I want something with a modern look and feel, not too conservative. This will be used for potential employers and freelance work.

Industry/Entity Type

Business

Contact Information for Business Card

Front should have my logo and name. The back should have all my personal information which would include: name: Tom Brevardi, phone: 570-614-9083, email: tombrevardi@mailwisp.com, website url: www.tombrevardi.com, logo, web developer.

Font styles to use
Sans Serif

Requirements
Must have
• Must include my logo. The color palette base color will be the logo color.

```html
<!DOCTYPE html>
<html lang="en">
<head>
<meta charset="utf-8">
<title>Tom Brevardi — Business Card</title>
<link rel="stylesheet" href="https://fonts.googleapis.com/css2?family=Source+Sans+3:wght@300;400;700&display=swap">
<style>
  :root {
    --backdrop: #a3a3a1;
    --card: #0f0f0f;
    --card-edge: #1a1a1a;
    --accent: #5fc6ad;
    --text-light: #e6e6e6;
    --rule: #2a2a2a;
  }
  * { box-sizing: border-box; margin: 0; padding: 0; }
  html, body {
    width: 1200px;
    height: 900px;
    overflow: hidden;
    background: var(--backdrop);
    font-family: "Source Sans 3", "Myriad Pro", Arial, sans-serif;
  }
  .sheet {
    position: relative;
    width: 1200px;
    height: 900px;
  }
  .card {
    position: absolute;
    left: 320px;
    width: 560px;
    height: 320px;
    background: radial-gradient(ellipse at 60% 30%, var(--card-edge), var(--card) 70%);
    box-shadow: 0 6px 18px rgba(0,0,0,0.25);
  }
  .card--front { top: 110px; }
  .card--back { top: 470px; }

  /* Mark: plain ring with name */
  .mark {
    position: absolute;
    width: 132px;
    height: 132px;
    border: 9px solid var(--accent);
    border-radius: 50%;
    display: flex;
    align-items: center;
    justify-content: center;
  }
  .mark__name {
    color: var(--accent);
    font-weight: 700;
    font-size: 20px;
    letter-spacing: 0.2px;
  }
  .card--front .mark { left: 214px; top: 40px; }
  .card--back .mark { left: 390px; top: 36px; }

  .front-identity {
    position: absolute;
    left: 0;
    right: 0;
    top: 196px;
    text-align: center;
    color: var(--accent);
  }
  .front-identity .name {
    font-weight: 700;
    font-size: 22px;
    line-height: 1.1;
  }
  .front-identity .role {
    font-weight: 400;
    font-size: 19px;
    margin-top: 2px;
  }

  .back-identity {
    position: absolute;
    left: 44px;
    top: 110px;
  }
  .back-identity .name {
    color: var(--accent);
    font-weight: 700;
    font-size: 21px;
    line-height: 1.1;
  }
  .back-identity .role {
    color: var(--text-light);
    font-weight: 300;
    font-size: 17px;
    margin-top: 2px;
  }
  .divider {
    position: absolute;
    left: 44px;
    right: 44px;
    top: 186px;
    height: 1px;
    background: var(--rule);
  }
  .contacts {
    position: absolute;
    right: 30px;
    top: 206px;
    list-style: none;
    text-align: right;
  }
  .contacts li {
    display: flex;
    justify-content: flex-end;
    align-items: center;
    gap: 10px;
    color: var(--text-light);
    font-size: 17px;
    line-height: 23px;
  }
  .contacts svg {
    width: 12px;
    height: 12px;
    fill: var(--accent);
  }
</style>
</head>
<body>
<main class="sheet">
  <section class="card card--front" aria-label="Card front">
    <div class="mark"><span class="mark__name">Brevardi</span></div>
    <div class="front-identity">
      <p class="name">Tom Brevardi</p>
      <p class="role">Front-End Developer</p>
    </div>
  </section>

  <section class="card card--back" aria-label="Card back">
    <div class="back-identity">
      <p class="name">Tom Brevardi</p>
      <p class="role">Front-End Developer</p>
    </div>
    <div class="mark"><span class="mark__name">Brevardi</span></div>
    <div class="divider"></div>
    <ul class="contacts">
      <li>570-614-9083
        <svg viewBox="0 0 24 24" aria-hidden="true"><path d="M6.6 10.8a15 15 0 0 0 6.6 6.6l2.2-2.2c.3-.3.7-.4 1-.2 1.1.4 2.3.6 3.6.6.6 0 1 .4 1 1V20c0 .6-.4 1-1 1A17 17 0 0 1 3 4c0-.6.4-1 1-1h3.5c.6 0 1 .4 1 1 0 1.3.2 2.5.6 3.6.1.3 0 .7-.2 1z"/></svg>
      </li>
      <li>tombrevardi@mailwisp.com
        <svg viewBox="0 0 24 24" aria-hidden="true"><path d="M2 5h20v14H2z M3.5 6.5 12 13l8.5-6.5" /><path d="M2 5l10 8 10-8v2l-10 8L2 7z" fill="#0f0f0f"/></svg>
      </li>
      <li>www.tombrevardi.com
        <svg viewBox="0 0 24 24" aria-hidden="true"><circle cx="12" cy="12" r="10"/><path d="M2 12h20M12 2c3 3 3 17 0 20M12 2c-3 3-3 17 0 20M4 7h16M4 17h16" stroke="#0f0f0f" stroke-width="1.5" fill="none"/></svg>
      </li>
    </ul>
  </section>
</main>
</body>
</html>
```